Maplerise Trading Inc. needs an innovative idea for letterhead and visiting cards.

Maplerise Trading Inc. is a Canadian brand since 2007. It is a renown dealer of kids and office furniture locally. Moreover, exporting electric fixtures e.g. switches, LED's, down-lights etc. to Middle East and Africa. We have initiated a number of steps including re-branding, to boost our export in 2020. We have successfully designed our new logo a few months ago through 'Artfolio' and now we are looking for an innovative idea for a letterhead.
Some key points:
• Red, black and white are the three colors used in all our packaging and furniture. (grey is optional)
• Shouldn’t be too wide.
• Use of watermark is preferable.
• You can visit our North American site at www.mapleriseinc.com. Export website of the company will be launched soon. www.mapleriseinc.ca
• Same letterhead will be used locally and internationally.
• Our new logo and sample packaging is attached.

```html
<!DOCTYPE html>
<html lang="en">
<head>
<meta charset="utf-8">
<title>Maplerise Trading – Visiting Card</title>
<link rel="stylesheet" href="https://fonts.googleapis.com/css2?family=Roboto:wght@400;500;700&display=swap">
<style>
  :root {
    --red: #a3161b;
    --ink: #2b2b2b;
    --grey: #4a4a4a;
    --paper: #ffffff;
    --card-dark: #262626;
    --stage: #d9d9d9;
    --mark-faint: #f5e6e1;
    --mark-faint-grey: #ececec;
  }
  * { box-sizing: border-box; margin: 0; padding: 0; }
  html, body { width: 1200px; height: 1004px; overflow: hidden; }
  body {
    background: var(--stage);
    font-family: "Roboto", Arial, sans-serif;
    display: flex; flex-direction: column; align-items: center; justify-content: center;
    gap: 60px;
  }
  .card {
    position: relative; width: 700px; height: 400px; overflow: hidden;
    box-shadow: 0 6px 20px rgba(0,0,0,.18);
  }
  .card-front { background: var(--paper); }
  .card-back { background: var(--card-dark); display: flex; align-items: center; justify-content: center; }

  .brand { position: absolute; left: 44px; top: 40px; display: flex; align-items: center; gap: 14px; }
  .brand-square { width: 52px; height: 52px; border: 3px solid var(--red); border-radius: 6px; }
  .brand-name { font-size: 30px; font-weight: 400; color: var(--grey); letter-spacing: 1px; text-transform: uppercase; line-height: 1; }

  .person { position: absolute; left: 44px; top: 128px; }
  .person-name { font-size: 30px; font-weight: 700; color: var(--red); }
  .person-role { font-size: 18px; color: var(--ink); margin-top: 2px; }

  .contact { position: absolute; left: 44px; top: 214px; font-size: 17px; color: var(--ink); line-height: 1.55; }
  .address { margin-bottom: 6px; }
  .contact-row { display: flex; align-items: center; gap: 10px; }
  .contact-row svg { width: 14px; height: 14px; flex: none; }
  .web-accent { color: var(--red); }

  .watermark { position: absolute; right: -30px; bottom: -30px; width: 330px; height: 230px; }
  .watermark-square { position: absolute; right: 0; bottom: 0; width: 230px; height: 230px; border: 18px solid var(--mark-faint-grey); border-radius: 24px; }
  .watermark-name { position: absolute; right: 60px; bottom: 90px; font-size: 54px; font-weight: 700; color: var(--mark-faint); text-transform: uppercase; }

  .back-brand { display: flex; align-items: center; gap: 18px; }
  .back-square { width: 70px; height: 70px; border: 3px solid #5a5a5a; border-radius: 10px; }
  .back-name { font-size: 34px; font-weight: 500; color: #6a6a6a; text-transform: uppercase; letter-spacing: 1px; }
</style>
</head>
<body>
  <section class="card card-front">
    <div class="watermark" aria-hidden="true">
      <div class="watermark-square"></div>
      <div class="watermark-name">Maplerise</div>
    </div>

    <div class="brand">
      <div class="brand-square"></div>
      <div class="brand-name">Maplerise Trading</div>
    </div>

    <div class="person">
      <div class="person-name">Daniel Whitmore</div>
      <div class="person-role">Owner</div>
    </div>

    <div class="contact">
      <div class="address">418, Harbour Street<br>Halifax NS B3H 1A1, CA</div>
      <div class="contact-row">
        <svg viewBox="0 0 16 16"><path fill="var(--red)" d="M3.6 1.5l2.3 2.6-1.2 1.6c.9 2 2.5 3.6 4.5 4.5l1.6-1.2 2.6 2.3-1.3 2.2C7 13.3 2.7 9 2.5 3z"/></svg>
        <span>(902) 555-0147</span>
      </div>
      <div class="contact-row">
        <svg viewBox="0 0 16 16"><rect x="1" y="3" width="14" height="10" fill="var(--red)"/><path d="M1 3l7 6 7-6" fill="none" stroke="#fff" stroke-width="1.3"/></svg>
        <span>daniel@mapleriseinc.com</span>
      </div>
      <div class="contact-row">
        <svg viewBox="0 0 16 16"><circle cx="8" cy="8" r="6.5" fill="var(--red)"/><path d="M1.5 8h13M8 1.5c-3 3.5-3 9.5 0 13M8 1.5c3 3.5 3 9.5 0 13" fill="none" stroke="#fff" stroke-width="1"/></svg>
        <span>www.<span class="web-accent">mapleriseinc</span>.com</span>
      </div>
    </div>
  </section>

  <section class="card card-back">
    <div class="back-brand">
      <div class="back-square"></div>
      <div class="back-name">Maplerise Trading</div>
    </div>
  </section>
</body>
</html>
```